Dog grooming business card
This is a business card for m dog grooming business like it say above.
In the priorities box below I will have the text that I want on the card.

Industry/Entity Type

Business

Colors

Designer to choose colors to be used in the design.

Requirements
Must have
• My logo and the insurance stamp must be on the card.

Text it must have :

Professional grooming services
Email: lindomerfield@brightmail.example
Text or call 1 705 318 6052
KSR certified/member
Pet first aid certified
Next appointment ___________________________________
Nice to have
• Greens to match my logo

```html
<!DOCTYPE html>
<html lang="en">
<head>
<meta charset="utf-8">
<title>Lindo Merfield – Professional Grooming Services</title>
<link rel="stylesheet" href="https://fonts.googleapis.com/css2?family=Quattrocento:wght@400;700&family=Josefin+Sans:wght@300;400&family=Open+Sans:wght@700;800&display=swap">
<style>
  :root {
    --leaf: #9cc23a;
    --leaf-deep: #8db32e;
    --ink: #000000;
    --paper: #ffffff;
    --bg-top: #ffffff;
    --bg-bottom: #cadf92;
    --badge-blue: #2a6fb8;
  }
  * { margin: 0; padding: 0; box-sizing: border-box; }
  html, body { width: 1200px; height: 1000px; overflow: hidden; }
  body {
    position: relative;
    background: linear-gradient(180deg, var(--bg-top) 0%, var(--bg-bottom) 100%);
    font-family: "Josefin Sans", sans-serif;
  }

  /* ---------- front of card ---------- */
  .card-front {
    position: absolute; left: 244px; top: 26px; width: 713px; height: 407px;
    overflow: hidden; background: var(--leaf);
  }
  .card-front__dark { position: absolute; inset: 0; }
  .brand {
    position: absolute; left: 0; right: 0; top: 30px; text-align: center;
  }
  .brand__dot {
    width: 72px; height: 72px; border-radius: 50%;
    background: var(--leaf); margin: 0 auto 14px;
  }
  .brand__name {
    font-family: "Quattrocento", serif; font-weight: 700;
    font-size: 34px; color: var(--leaf); letter-spacing: 0.5px;
  }
  .tagline {
    position: absolute; left: 0; right: 0; top: 183px; text-align: center;
    font-family: "Quattrocento", serif; font-size: 35px; letter-spacing: 2px;
    color: var(--leaf);
  }
  .contact {
    position: absolute; left: 0; right: 0; text-align: center; color: var(--paper);
    font-size: 27px; font-weight: 300;
  }
  .contact--email { top: 252px; }
  .contact--phone { top: 295px; font-size: 30px; }
  .contact__label {
    font-family: "Quattrocento", serif; font-weight: 700; color: var(--leaf);
    font-size: 23px; margin-right: 6px;
  }
  .credential {
    position: absolute; top: 361px; font-size: 23px; color: var(--ink); font-weight: 400;
  }
  .credential--member { left: 88px; }
  .credential--firstaid { left: 421px; }

  /* ---------- back of card ---------- */
  .card-back {
    position: absolute; left: 244px; top: 522px; width: 713px; height: 408px;
    overflow: hidden;
  }
  .card-back svg { display: block; }
  .appt-heading {
    font-family: "Open Sans", sans-serif; font-weight: 800; font-size: 23px;
    fill: var(--paper);
  }
  .day-label { font-family: "Open Sans", sans-serif; font-weight: 700; font-size: 14px; fill: #222; }
  .slot-label { font-family: "Open Sans", sans-serif; font-weight: 700; font-size: 14px; fill: #222; }
</style>
</head>
<body>

<section class="card-front" aria-label="Business card front">
  <svg class="card-front__dark" width="713" height="407" viewBox="0 0 713 407" aria-hidden="true">
    <path d="M0 0 H713 V310 Q356 380 0 312 Z" fill="var(--ink)"/>
  </svg>
  <div class="brand">
    <div class="brand__dot"></div>
    <div class="brand__name">Lindo Merfield</div>
  </div>
  <h1 class="tagline">Professional Grooming Services</h1>
  <p class="contact contact--email"><span class="contact__label">Email:</span>lindomerfield@brightmail.example</p>
  <p class="contact contact--phone"><span class="contact__label">Text or call:</span>1 705 318 6052</p>
  <p class="credential credential--member">KSR certified/member</p>
  <p class="credential credential--firstaid">Pet first aid certified</p>
</section>

<section class="card-back" aria-label="Appointment card back">
  <svg width="713" height="408" viewBox="0 0 713 408">
    <rect class="pattern-field" width="713" height="408" fill="var(--leaf)" role="img" aria-label="Repeating pattern of small poodle silhouettes with bows"/>
    <text class="appt-heading" x="354" y="50" text-anchor="middle">YOUR NEXT APPOINTMENT IS ON:</text>

    <circle cx="363" cy="228" r="165" fill="var(--paper)"/>

    <g class="day-buttons" fill="var(--paper)">
      <circle cx="207" cy="94" r="27"/>
      <circle cx="164" cy="157" r="27"/>
      <circle cx="151" cy="226" r="27"/>
      <circle cx="163" cy="290" r="27"/>
      <circle cx="197" cy="356" r="27"/>
    </g>
    <text class="day-label" x="207" y="99" text-anchor="middle">MON</text>
    <text class="day-label" x="164" y="162" text-anchor="middle">TUE</text>
    <text class="day-label" x="151" y="231" text-anchor="middle">WED</text>
    <text class="day-label" x="163" y="295" text-anchor="middle">THU</text>
    <text class="day-label" x="197" y="361" text-anchor="middle">FRI</text>

    <line x1="241" y1="169" x2="451" y2="169" stroke="var(--leaf)" stroke-width="2"/>
    <text class="slot-label" x="213" y="245">AT</text>
    <line x1="241" y1="246" x2="472" y2="246" stroke="var(--leaf)" stroke-width="2"/>
    <text class="slot-label" x="389" y="235">AM</text>
    <text class="slot-label" x="444" y="235">PM</text>

    <rect class="insurance-badge" x="256" y="279" width="188" height="84" rx="14" fill="var(--paper)" stroke="var(--badge-blue)" stroke-width="2"/>
    <rect x="276" y="300" width="148" height="42" rx="6" fill="var(--badge-blue)" opacity="0.85"/>

    <circle cx="567" cy="214" r="75" fill="var(--leaf)" stroke="var(--paper)" stroke-width="5"/>
    <circle cx="567" cy="214" r="58" fill="var(--leaf-deep)" role="img" aria-label="Brand emblem: poodle silhouette with a bow"/>
  </svg>
</section>

</body>
</html>
```